Flyer for Yoga and IronForge.

Just initial idea and open to creativity: I am thinking right half of flyer to be IronForge info and left half to be Yoga info.
Feel free to add text as needed but would like following:
Basic text: LotusKeMo $69/mo unlimited sessions.
LotusKEMO.com
IronForge: $99 intro session. Largest IronForge in Texas.
IronForgeKEMO.com

Located Kessel Midtown Houston (KEMO)
Address: 4180 Marlow Pkwy Houston, tx

Please submit any and all designs. Looking to get some great ideas!

Target Market(s)

Young professionals free spirited and fun atmosphere.

Colors
3176b5
85acd3
32a6d7
32b7a4
f59195
cde9f5
f04a50

Requirements
Must have
• Professional yet fun. Text should include:
LotusKeMo and IronForge KeMo taking each a half of the page seperatly get still be identifiable as one. Want to show there is two options for either yoga or IronForge or do both!
IronForge Intro is $99 adm yoga intro is $69.
Nice to have
• Also visit www.ironforgekemo.com for more ideas and info.

```html
<!DOCTYPE html>
<html lang="en">
<head>
<meta charset="utf-8">
<title>LotusKeMo &amp; IronForge KeMo Flyer</title>
<link href="https://fonts.googleapis.com/css2?family=Bitter:wght@400;600;700&family=Montserrat:wght@500&display=swap" rel="stylesheet">
<style>
  :root {
    --page-bg: #ece8e2;
    --yoga-blue: #2a77b7;
    --yoga-blue-soft: #85acd3;
    --forge-red: #ef4b52;
    --forge-red-soft: #f59195;
    --brand-red: #c4323f;
    --teal: #32b7b4;
    --white: #ffffff;
    --ink: #222222;
    --rule: #555555;
  }
  * { margin: 0; padding: 0; box-sizing: border-box; }
  html, body {
    width: 915px; height: 1200px; overflow: hidden;
    background: var(--page-bg);
  }
  .flyer {
    position: absolute; left: 44px; top: 14px;
    width: 690px; height: 977px;
    transform: scale(1.2); transform-origin: 0 0;
    background: var(--white);
    font-family: "Bitter", Georgia, serif;
    box-shadow: 0 2px 6px rgba(0,0,0,.2);
  }
  .half {
    position: absolute; top: 0; width: 345px; height: 910px; overflow: hidden;
  }
  .half--yoga { left: 0; background: var(--yoga-blue); }
  .half--forge { left: 345px; background: var(--forge-red); }
  .band { position: absolute; left: 0; top: 0; }
  .line {
    position: absolute; left: 0; width: 345px; text-align: center;
    color: var(--white); font-weight: 700; line-height: 1;
  }
  .offer-cta { top: 26px; font-size: 27px; }
  .offer-url { top: 84px; font-size: 27px; }
  .offer-price { top: 138px; font-size: 50px; }
  .offer-note { top: 194px; font-size: 29px; }
  .illustration {
    position: absolute; border-radius: 40px;
    background: radial-gradient(ellipse at center, rgba(255,255,255,.92) 0%, rgba(255,255,255,.55) 60%, rgba(255,255,255,0) 100%);
  }
  .illustration--yoga { left: 40px; top: 262px; width: 265px; height: 298px; }
  .illustration--forge { left: 80px; top: 340px; width: 225px; height: 350px; }
  .brand-mark {
    position: absolute; left: 0; width: 345px; text-align: center;
    font-weight: 700; color: var(--brand-red); line-height: 1;
  }
  .brand-dot {
    position: absolute; left: 149px; top: 618px; width: 34px; height: 34px;
    border-radius: 50%; background: var(--teal);
  }
  .rule { position: absolute; height: 1px; background: var(--rule); }
  .tagline {
    position: absolute; left: 0; width: 345px; text-align: center;
    font-family: "Montserrat", Arial, sans-serif; font-weight: 500;
    font-size: 8px; letter-spacing: 2.4px; color: var(--ink);
  }
  .footer {
    position: absolute; left: 0; top: 910px; width: 690px; height: 67px;
    display: flex; align-items: center; padding-left: 22px;
  }
  .footer__address { margin-left: 8px; font-size: 15.5px; color: var(--ink); font-weight: 400; }
  .footer__social { margin-left: auto; margin-right: 16px; display: flex; gap: 12px; }
  .footer__social span {
    width: 32px; height: 32px; border-radius: 5px; background: #9aa3ad;
  }
</style>
</head>
<body>
<main class="flyer">
  <section class="half half--yoga">
    <p class="line offer-cta">Try Free Class Today!</p>
    <p class="line offer-url">LotusKEMO.com</p>
    <p class="line offer-price">$69/month</p>
    <p class="line offer-note">unlimited sessions</p>
    <div class="illustration illustration--yoga" role="img" aria-label="White silhouette of a person meditating in lotus pose"></div>
    <svg class="band" width="345" height="910" viewBox="0 0 345 910">
      <polygon points="0,600 172,565 345,600 345,893 172,860 0,893" fill="#ffffff"/>
    </svg>
    <div class="rule" style="left:82px; top:648px; width:60px;"></div>
    <div class="rule" style="left:192px; top:648px; width:66px;"></div>
    <span class="brand-dot"></span>
    <p class="brand-mark" style="top:690px; font-size:52px;">LotusKeMo</p>
    <p class="tagline" style="top:808px;">KESSEL MIDTOWN HOUSTON</p>
    <div class="rule" style="left:82px; top:832px; width:176px;"></div>
  </section>

  <section class="half half--forge">
    <svg class="band" width="345" height="910" viewBox="0 0 345 910">
      <polygon points="0,20 172,53 345,20 345,295 172,338 0,295" fill="#ffffff"/>
    </svg>
    <p class="brand-mark" style="top:112px; font-size:52px;">IronForge</p>
    <p class="brand-mark" style="top:172px; font-size:52px;">KeMo</p>
    <div class="rule" style="left:85px; top:248px; width:175px;"></div>
    <p class="tagline" style="top:260px; font-size:7px;">KESSEL MIDTOWN HOUSTON</p>
    <div class="illustration illustration--forge" role="img" aria-label="White silhouette of an athlete lifting a barbell overhead in a lunge"></div>
    <p class="line offer-price" style="top:726px;">$99</p>
    <p class="line offer-note" style="top:776px;">intro session</p>
    <p class="line offer-url" style="top:830px;">IronForgeKEMO.com</p>
  </section>

  <footer class="footer">
    <svg width="14" height="20" viewBox="0 0 14 20" aria-hidden="true">
      <path d="M7 0C3.1 0 0 3.1 0 7c0 5 7 13 7 13s7-8 7-13c0-3.9-3.1-7-7-7zm0 9.6A2.6 2.6 0 1 1 7 4.4a2.6 2.6 0 0 1 0 5.2z" fill="#222"/>
    </svg>
    <p class="footer__address">4180 Marlow Pkwy Houston, Kessel Midtown Houston (KEMO), Texas</p>
    <div class="footer__social" aria-label="Social links">
      <span></span><span></span><span></span>
    </div>
  </footer>
</main>
</body>
</html>
```